Harvest Road Formation *

need a book cover design
The information I would add at the back of the book would go this way.
A NEW EVANGELISTIC MOVEMENT IS COMING
Has God called you to be an Evangelist?
How do I know that I am called to be an Evangelist?
How long is the training?
How will God train me?
How do I prepare myself?
These are just a few of the common questions being asked concerning the Evangelistic ministry. This book
will answer your questions and help you to understand the training of the Evangelist.
Here are some key points that I would take you through:
- Who is an Evangelist
- Signs of the Evangelistic Calling
- Evangelistic Preparation
- Harvest Road Formation
- Evangelistic Key
I also attached a copy of how I want the front book cover design to look. I want the hand in the book cover to be deleted, I want the fire to burn up to the middle of the book cover. The name of the book at the below end of the book cover.
Colors
Designer to choose only greyscale colors for use in the design.

```html
<!DOCTYPE html>
<html lang="en">
<head>
<meta charset="utf-8">
<title>Harvest Road Formation – Book Cover</title>
<link href="https://fonts.googleapis.com/css2?family=Cinzel:wght@400;500&family=EB+Garamond:ital,wght@0,400;1,600&display=swap" rel="stylesheet">
<style>
  :root {
    --page: #ffffff;
    --ink: #111111;
    --body-ink: #2a2622;
    --accent: #a9653a;
    --bg-top: #e9e1d6;
    --bg-mid: #f3eee6;
    --bg-warm: #c98a52;
    --bg-deep: #8a4f26;
    --spine: #ffffff;
  }
  * { margin: 0; padding: 0; box-sizing: border-box; }
  html, body { width: 1200px; height: 1200px; overflow: hidden; background: var(--page); }
  .canvas { position: relative; width: 1200px; height: 1200px; background: var(--page); }
  .spread { position: absolute; left: 0; top: 158px; width: 1200px; height: 882px; }

  .panel { position: absolute; top: 0; height: 882px; overflow: hidden; }
  .panel-back { left: 0; width: 571px; }
  .panel-spine { left: 571px; width: 59px; background: var(--spine); }
  .panel-front { left: 630px; width: 570px; }

  .backdrop {
    position: absolute; inset: 0;
    background:
      radial-gradient(ellipse 60% 30% at 50% 100%, rgba(138,79,38,0.55), transparent 70%),
      linear-gradient(to bottom, var(--bg-top) 0%, var(--bg-mid) 35%, #efe6da 62%, var(--bg-warm) 80%, var(--bg-deep) 100%);
  }
  .backdrop-front {
    background:
      radial-gradient(ellipse 22% 40% at 55% 72%, rgba(40,40,48,0.35), transparent 70%),
      radial-gradient(ellipse 60% 30% at 50% 100%, rgba(138,79,38,0.55), transparent 70%),
      linear-gradient(to bottom, var(--bg-top) 0%, var(--bg-mid) 35%, #efe6da 62%, var(--bg-warm) 80%, var(--bg-deep) 100%);
  }

  /* Back cover */
  .back-copy { position: absolute; left: 0; top: 0; width: 571px; font-family: "EB Garamond", Georgia, serif; color: var(--body-ink); }
  .back-headline {
    position: absolute; left: 0; width: 580px; top: 96px; text-align: center;
    font-style: italic; font-weight: 600; font-size: 21px; line-height: 29px; color: var(--ink); letter-spacing: 0.3px;
  }
  .back-questions { position: absolute; left: 0; width: 580px; top: 178px; text-align: center; list-style: none; font-size: 16px; line-height: 26.4px; }
  .back-intro { position: absolute; left: 43px; width: 494px; top: 326px; font-size: 16px; line-height: 22.4px; text-align: justify; }
  .back-lead { position: absolute; left: 43px; top: 416px; font-size: 16px; line-height: 22px; }
  .back-points { position: absolute; left: 62px; top: 469px; list-style: none; font-size: 16px; line-height: 32px; }
  .barcode-area { position: absolute; left: 363px; top: 732px; width: 185px; height: 116px; background: #ffffff; }

  /* Spine */
  .spine-title, .spine-author {
    position: absolute; left: 50%; white-space: nowrap;
    transform-origin: left top; transform: rotate(90deg) translateY(-50%);
  }
  .spine-title { top: 38px; font-family: "Cinzel", serif; font-size: 29px; color: var(--ink); margin-left: 0; }
  .spine-author { top: 674px; font-family: "Cinzel", serif; font-size: 20px; color: var(--accent); }

  /* Front */
  .front-author {
    position: absolute; left: 0; width: 570px; top: 50px; text-align: center;
    font-family: "Cinzel", serif; font-size: 39px; color: var(--accent); letter-spacing: 1px;
  }
  .front-title {
    position: absolute; left: 0; width: 570px; top: 170px; text-align: center;
    font-family: "Cinzel", serif; font-weight: 400; font-size: 74px; line-height: 112px; color: var(--ink);
  }
</style>
</head>
<body>
<div class="canvas">
  <div class="spread">
    <section class="panel panel-back">
      <div class="backdrop" role="img" aria-label="Soft-focus photograph of a bright church interior with wooden pews"></div>
      <div class="back-copy">
        <h2 class="back-headline">A NEW EVANGELISTIC MOVEMENT<br>IS COMING</h2>
        <ul class="back-questions">
          <li>Has God called you to be an Evangelist?</li>
          <li>How do I know that I am called to be an Evangelist?</li>
          <li>How long is the training?</li>
          <li>How will God train me?</li>
          <li>How do I prepare myself?</li>
        </ul>
        <p class="back-intro">These are just a few of the common questions being asked concerning the Evangelistic ministry. This book will answer your questions and help you to understand the training of the Evangelist.</p>
        <p class="back-lead">Here are some key points that I would take you through:</p>
        <ul class="back-points">
          <li>- Who is an Evangelist</li>
          <li>- Signs of the Evangelistic Calling</li>
          <li>- Evangelistic Preparation</li>
          <li>- Harvest Road Formation</li>
          <li>- Evangelistic Key</li>
        </ul>
        <div class="barcode-area"></div>
      </div>
    </section>

    <section class="panel panel-spine">
      <div class="spine-title">HARVEST ROAD FORMATION</div>
      <div class="spine-author">AUTHOR NAME</div>
    </section>

    <section class="panel panel-front">
      <div class="backdrop backdrop-front" role="img" aria-label="Close-up photograph of a stage microphone in front of a blurred church interior with pews"></div>
      <div class="front-author">AUTHOR NAME</div>
      <h1 class="front-title">Harvest Road<br>Formation</h1>
    </section>
  </div>
</div>
</body>
</html>
```